Award-winnning Estate Agent needs a premium version of their 'For Sale' board design

We need a premium option for our 'For Sale' board design. We have a standard board that is attached to this brief, but were are looking to have a premium design version that we will use when selling exclusive properties. Our company name is Harbour Lane Estates and the name for this is exclusive selection is: 'The Harbour Collection'. The design needs to work with our current brand, but have a distinctive PREMIUM feel to it. I have uploaded the barnd guidelines and also some of the exisisting logo variations. We do NOT need a new logo but feel free to play around with colours, fonts, sizes etc. for the sign.

Target Market(s)

Property buyers & house hunters

Industry/Entity Type

Real Estate - Residential Property

Font styles to use
Sans Serif

Requirements
Must have
• A premium fee, must be square design, must be easy to read when driving past the sign
Nice to have
• I'm open ot ideas

```html
<!DOCTYPE html>
<html lang="en">
<head>
<meta charset="utf-8">
<title>Harbour Lane Estates – For Sale Board</title>
<link href="https://fonts.googleapis.com/css2?family=Inter:wght@200;300;700&display=swap" rel="stylesheet">
<style>
  :root {
    --navy-deep: #0c0f50;
    --navy-band: #171d63;
    --blue-glow: #1172bd;
    --white: #ffffff;
    --headline-ink: #0c0f50;
  }
  * { margin: 0; padding: 0; box-sizing: border-box; }
  html, body {
    width: 1200px;
    height: 1200px;
    overflow: hidden;
    background: var(--navy-deep);
    font-family: "Inter", "Helvetica Neue", Arial, sans-serif;
  }
  .board {
    position: relative;
    width: 1200px;
    height: 1200px;
    background: var(--navy-deep);
    overflow: hidden;
  }
  .board__header {
    position: absolute;
    left: 0; top: 0;
    width: 100%;
    height: 319px;
    background: radial-gradient(ellipse 520px 420px at 595px 0, var(--blue-glow) 0%, #1a3f84 45%, var(--navy-deep) 100%);
  }
  .brand-name {
    position: absolute;
    left: 0; width: 100%;
    top: 205px;
    text-align: center;
    color: var(--white);
    font-weight: 700;
    font-size: 54px;
    letter-spacing: -0.5px;
    line-height: 1;
  }
  .collection-band {
    position: absolute;
    left: 0; top: 319px;
    width: 100%;
    height: 150px;
    background: var(--white);
  }
  .collection-title {
    position: absolute;
    left: 0; width: 100%;
    top: 338px;
    text-align: center;
    color: var(--headline-ink);
    font-weight: 200;
    font-size: 104px;
    letter-spacing: -3px;
    line-height: 1;
  }
  .lower-band {
    position: absolute;
    left: 0; top: 761px;
    width: 100%;
    height: 439px;
    background: var(--navy-band);
  }
  .lower-band__rule {
    position: absolute;
    left: 0; top: 869px;
    width: 100%;
    height: 22px;
    background: var(--navy-deep);
  }
  .status {
    position: absolute;
    left: 0; width: 100%;
    top: 732px;
    text-align: center;
    color: var(--white);
    font-weight: 700;
    font-size: 212px;
    letter-spacing: -6px;
    line-height: 1;
  }
  .status-underline {
    position: absolute;
    left: 86px; top: 929px;
    width: 1031px;
    height: 8px;
    background: var(--white);
  }
  .phone {
    position: absolute;
    left: 0; width: 100%;
    top: 955px;
    text-align: center;
    color: var(--white);
    font-weight: 300;
    font-size: 102px;
    letter-spacing: -1px;
    line-height: 1;
    word-spacing: 18px;
  }
  .website {
    position: absolute;
    left: 0; width: 100%;
    top: 1104px;
    text-align: center;
    color: var(--white);
    font-weight: 200;
    font-size: 42px;
    letter-spacing: -1px;
    line-height: 1;
  }
</style>
</head>
<body>
  <main class="board">
    <header class="board__header">
      <p class="brand-name">Harbour Lane Estates</p>
    </header>

    <div class="collection-band"></div>
    <h2 class="collection-title">The Harbour Collection</h2>

    <div class="lower-band"></div>
    <div class="lower-band__rule"></div>

    <h1 class="status">FOR SALE</h1>
    <div class="status-underline"></div>
    <p class="phone">01632 960418</p>
    <p class="website">www.harbourlaneestates.co.uk</p>
  </main>
</body>
</html>
```